Income Tax Business Cards - Updates

Need to update these business cards while keeping all the same wording but just update them and make them look nicer and more modern/ on brand with our brand.

Industry/Entity Type

finance

Contact Information for Business Card

we have multiple locations so will just need to easily be able to change the address and phone numbers

Colors

Designer to choose colors to be used in the design.

```html
<!DOCTYPE html>
<html lang="en">
<head>
<meta charset="utf-8">
<title>Tax Advance Business Cards</title>
<link rel="stylesheet" href="https://fonts.googleapis.com/css2?family=Montserrat:wght@600;700;800;900&family=Lato:wght@400&display=swap">
<style>
  :root {
    --green: #0b5130;
    --red: #c41f2a;
    --white: #ffffff;
    --grey: #5c5f63;
    --backdrop: #2c2e33;
    --card-w: 700px;
    --card-h: 400px;
    --radius: 28px;
  }
  * { box-sizing: border-box; margin: 0; padding: 0; }
  html, body {
    width: 1200px; height: 952px; overflow: hidden;
    background: var(--backdrop);
  }
  body {
    display: flex; flex-direction: column; align-items: center; justify-content: center;
    gap: 56px;
    font-family: "Montserrat", sans-serif;
  }
  .card {
    position: relative;
    width: var(--card-w); height: var(--card-h);
    border-radius: var(--radius);
    overflow: hidden;
    background: var(--white);
    box-shadow: 0 14px 30px rgba(0,0,0,.45);
  }
  .band { position: absolute; left: 0; right: 0; display: flex; align-items: center; justify-content: center; color: var(--white); text-transform: uppercase; }

  /* Front */
  .front .band-headline { top: 0; height: 92px; background: var(--red); font-weight: 900; font-size: 50px; letter-spacing: .5px; }
  .front .band-call { top: 92px; height: 70px; background: var(--green); font-weight: 800; font-size: 33px; letter-spacing: 1px; }
  .offer { position: absolute; left: 40px; top: 190px; text-transform: uppercase; line-height: 1; }
  .offer-lead { color: var(--green); font-weight: 900; font-size: 60px; }
  .offer-amount { color: var(--red); font-weight: 900; font-size: 72px; margin-top: 4px; }
  .offer-note { color: var(--green); font-weight: 800; font-size: 17px; margin-top: 8px; letter-spacing: .5px; }

  .brand { position: absolute; display: flex; flex-direction: column; align-items: center; }
  .brand-row { display: flex; align-items: center; gap: 12px; }
  .brand-dot { width: 18px; height: 18px; border-radius: 50%; background: var(--red); }
  .brand-name { color: var(--green); font-weight: 700; font-size: 30px; }
  .front .brand { right: 46px; top: 280px; }
  .brand-url { color: var(--red); font-weight: 600; font-size: 17px; margin-top: 8px; letter-spacing: .5px; }

  /* Back */
  .back .band-offer { top: 0; height: 184px; background: var(--green); flex-direction: column; gap: 4px; }
  .back .offer-amount-line { color: var(--red); font-weight: 900; font-size: 56px; line-height: 1; }
  .back .offer-title { font-weight: 900; font-size: 40px; line-height: 1; }
  .terms { display: flex; align-items: center; gap: 12px; width: 88%; margin-top: 8px; font-weight: 700; font-size: 13px; letter-spacing: .8px; }
  .terms::before, .terms::after { content: ""; flex: 1; height: 1px; background: rgba(255,255,255,.7); }
  .back .band-estimates { top: 184px; height: 54px; background: var(--red); font-weight: 900; font-size: 28px; letter-spacing: 1px; }

  .locations { position: absolute; left: 40px; top: 268px; list-style: none; display: flex; flex-direction: column; gap: 16px; }
  .location { display: flex; align-items: center; gap: 10px; font-family: "Lato", sans-serif; font-size: 16px; color: var(--grey); }
  .location svg { width: 20px; height: 20px; flex: none; }
  .back .brand { right: 50px; top: 290px; }
</style>
</head>
<body>

<section class="card front" aria-label="Card front">
  <div class="band band-headline">File your taxes here</div>
  <div class="band band-call">Call now : (555)555-5555</div>
  <div class="offer">
    <div class="offer-lead">Up to</div>
    <div class="offer-amount">$6,000</div>
    <div class="offer-note">Same day advance</div>
  </div>
  <div class="brand">
    <div class="brand-row"><span class="brand-dot"></span><span class="brand-name">Keystone Tax Group</span></div>
  </div>
</section>

<section class="card back" aria-label="Card back">
  <div class="band band-offer">
    <div class="offer-amount-line">Up to $6,000</div>
    <div class="offer-title">Same day advance</div>
    <div class="terms">On approved tax returns!</div>
  </div>
  <div class="band band-estimates">Free estimates!</div>
  <ul class="locations">
    <li class="location"><svg viewBox="0 0 20 20" aria-hidden="true"><rect width="20" height="20" rx="4" fill="#0b5130"/><path d="M10 4a4 4 0 0 0-4 4c0 3 4 8 4 8s4-5 4-8a4 4 0 0 0-4-4z" fill="#fff"/><circle cx="10" cy="8" r="1.6" fill="#0b5130"/></svg>Address Line 1</li>
    <li class="location"><svg viewBox="0 0 20 20" aria-hidden="true"><rect width="20" height="20" rx="4" fill="#0b5130"/><path d="M10 4a4 4 0 0 0-4 4c0 3 4 8 4 8s4-5 4-8a4 4 0 0 0-4-4z" fill="#fff"/><circle cx="10" cy="8" r="1.6" fill="#0b5130"/></svg>Address Line 2</li>
    <li class="location"><svg viewBox="0 0 20 20" aria-hidden="true"><rect width="20" height="20" rx="4" fill="#0b5130"/><path d="M10 4a4 4 0 0 0-4 4c0 3 4 8 4 8s4-5 4-8a4 4 0 0 0-4-4z" fill="#fff"/><circle cx="10" cy="8" r="1.6" fill="#0b5130"/></svg>Address Line 3</li>
  </ul>
  <div class="brand">
    <div class="brand-row"><span class="brand-dot"></span><span class="brand-name">Keystone Tax Group</span></div>
    <div class="brand-url">www.keystonetax.com</div>
  </div>
</section>

</body>
</html>
```